RW Framewell Inc Business cards

We need business cards using our existing logo but slightly modified. Right now the logo says RW Bedrock Masonry. We want to keep the RW part of the design, but replace the Bedrock Masonry portion with "FRAMEWELL". Please see the attached file.
Ideally this would be a blank template so we can add Different Names, titles, and phone numbers later.
On the one side we want only the logo and on the other side the detail. I'm attaching an example for you to see.
Please reach out with any other questions. Our address and other details will be given out once we find a design we like.

Target Market(s)

Construction Industry

```html
<!DOCTYPE html>
<html lang="en">
<head>
<meta charset="utf-8">
<title>RW Framewell Inc – Business Cards</title>
<link rel="stylesheet" href="https://fonts.googleapis.com/css2?family=Montserrat:wght@400;700&family=Figtree:wght@400;700&display=swap">
<style>
  :root {
    --brand-blue: #1b70b5;
    --brand-grey: #7a7b7d;
    --card-white: #f6f5f3;
    --ink: #333436;
    --backdrop: #dcdcdc;
  }
  * { margin: 0; padding: 0; box-sizing: border-box; }
  html, body { width: 1113px; height: 1200px; overflow: hidden; }
  body { background: var(--backdrop); position: relative; font-family: "Figtree", sans-serif; }

  .card {
    position: absolute;
    width: 707px;
    height: 405px;
    border-radius: 21px;
    overflow: hidden;
  }
  .card--front { left: 203px; top: 144px; background: var(--brand-blue); }
  .card--back  { left: 202px; top: 644px; background: var(--card-white); }

  .wordmark { position: absolute; font-family: "Montserrat", sans-serif; }
  .wordmark__initials { font-weight: 700; line-height: 1; display: block; }
  .wordmark__name { font-weight: 400; display: block; line-height: 1; }

  .card--front .wordmark { left: 168px; top: 100px; width: 375px; text-align: center; color: #ffffff; }
  .card--front .wordmark__initials { font-size: 180px; letter-spacing: 6px; }
  .card--front .wordmark__name { font-size: 35px; letter-spacing: 17px; margin-top: 14px; margin-right: -17px; }

  .card--back .wordmark { left: 88px; top: 128px; width: 248px; text-align: center; }
  .card--back .wordmark__initials { font-size: 122px; color: var(--brand-blue); letter-spacing: 4px; }
  .card--back .wordmark__name { font-size: 23px; letter-spacing: 11.5px; margin-top: 8px; margin-right: -11.5px; color: var(--brand-grey); }

  .divider { position: absolute; left: 363px; top: 96px; width: 2px; height: 217px; background: var(--brand-blue); }

  .details { position: absolute; left: 384px; top: 92px; color: var(--ink); }
  .details__name { font-weight: 700; font-size: 27px; letter-spacing: 0.2px; line-height: 1.2; }
  .details__first { color: var(--brand-blue); }
  .details__last { color: var(--brand-grey); }
  .details__title { font-size: 20px; line-height: 1.2; margin-top: 1px; }
  .details__address { font-size: 20px; line-height: 27px; margin-top: 14px; }

  .contact { list-style: none; margin-top: 16px; }
  .contact__item { display: flex; align-items: center; font-size: 20px; height: 31px; }
  .contact__icon { width: 18px; height: 18px; margin-right: 9px; flex: none; }
  .contact__accent { color: var(--brand-blue); }
</style>
</head>
<body>

<section class="card card--front" aria-label="Card front">
  <div class="wordmark">
    <span class="wordmark__initials">RW</span>
    <span class="wordmark__name">FRAMEWELL</span>
  </div>
</section>

<section class="card card--back" aria-label="Card back">
  <div class="wordmark">
    <span class="wordmark__initials">RW</span>
    <span class="wordmark__name">FRAMEWELL</span>
  </div>

  <div class="divider"></div>

  <div class="details">
    <p class="details__name"><span class="details__first">DANIEL</span> <span class="details__last">HOLLIS</span></p>
    <p class="details__title">Director</p>
    <p class="details__address">Street Name Ave, Suite 100<br>State, Zip code, Country</p>

    <ul class="contact">
      <li class="contact__item">
        <svg class="contact__icon" viewBox="0 0 24 24" aria-hidden="true">
          <path fill="#1b70b5" d="M6.6 10.8a15.1 15.1 0 0 0 6.6 6.6l2.2-2.2c.3-.3.7-.4 1-.2 1.1.4 2.3.6 3.6.6.6 0 1 .4 1 1V20c0 .6-.4 1-1 1A17 17 0 0 1 3 4c0-.6.4-1 1-1h3.5c.6 0 1 .4 1 1 0 1.3.2 2.5.6 3.6.1.3 0 .7-.2 1z"/>
          <path fill="none" stroke="#1b70b5" stroke-width="2" d="M14 3a7 7 0 0 1 7 7M14 7a3 3 0 0 1 3 3"/>
        </svg>
        555.014.2290
      </li>
      <li class="contact__item">
        <svg class="contact__icon" viewBox="0 0 24 24" aria-hidden="true">
          <rect x="2" y="5" width="20" height="14" rx="1" fill="#1b70b5"/>
          <path d="M3 6l9 7 9-7" fill="none" stroke="#f6f5f3" stroke-width="1.8"/>
        </svg>
        info@rwframewell.com
      </li>
      <li class="contact__item">
        <svg class="contact__icon" viewBox="0 0 24 24" aria-hidden="true">
          <circle cx="12" cy="12" r="10" fill="#1b70b5"/>
          <path d="M12 2v20M2 12h20M12 2c-4 4-4 16 0 20M12 2c4 4 4 16 0 20" fill="none" stroke="#f6f5f3" stroke-width="1.3"/>
        </svg>
        <span>www.<span class="contact__accent">rwframewell</span>.com</span>
      </li>
    </ul>
  </div>
</section>

</body>
</html>
```